Homepage Website Design for luxury picnic company

We need a homepage designed for a luxury picnic business to match our updated branding/logo which we're currently completing on ArtGatherly with another competition. Please see attached logo/colour example to use for now.

PLEASE NOTE: We are only after graphic design concepts as part of this competition. I will get another developer to actually code the website.

It is important that this website is very elegant/luxurious and stands out from a visual perspective. The images really need to match the content/sections also. The new branding colours are silver with a dark background. Please create the new website homepage to match these colours/branding.

Please create as many concepts as possible and then I will provide feedback from there

The website content including sections is here https://pages.velmoranote.com/doc/d/7kRtWq2mLp9XcVb4Hn8Js3Yd6Fg1Za5Qe0Uo2Ti/edit?mode=share

Images to use are located here https://vault.trenquilbox.com/vault/dirs/5HmQzR2-NcWy8Kp41-7VbLdTsXoeFj?mode=share and there is also lots of videos at this link which you can screenshot images out of if needed https://www.stashquarry.com/sh/k827trwm3hdz4/AACvnRt2Lm8WqPe5Xu9JdsYk?dl=0

Any questions please contact me

```html
<!DOCTYPE html>
<html lang="en">
<head>
<meta charset="utf-8">
<title>Picnic Wayfare – Luxury Picnics</title>
<link href="https://fonts.googleapis.com/css2?family=Poppins:wght@300;400;500;600;700&display=swap" rel="stylesheet">
<style>
:root{
  --orange:#f7931e;
  --orange-soft:#f6a623;
  --ink:#1e2024;
  --muted:#7d7f84;
  --white:#ffffff;
  --footer:#2c2f35;
  --footer-deep:#24272c;
  --field:#b9bcc1;
}
*{box-sizing:border-box;margin:0;padding:0}
html,body{width:1200px;height:4143px;overflow:hidden}
body{position:relative;background:#fff;font-family:'Poppins',sans-serif;color:var(--ink)}
.abs{position:absolute}
.center{text-align:center}
.btn{position:absolute;display:flex;align-items:center;justify-content:center;background:var(--orange);color:#fff;font-weight:600;border-radius:20px;font-size:12px}

/* hero */
.hero{left:0;top:0;width:1200px;height:600px;background:radial-gradient(ellipse at 35% 55%,#6b5642 0%,#3d3832 40%,#232529 80%);}
.brand{left:161px;top:34px;font-weight:700;font-size:14px;line-height:16px;color:#fff;letter-spacing:.3px}
.nav{left:343px;top:44px;display:flex;font-size:13px;color:#fff}
.nav span{position:absolute;white-space:nowrap}
.nav .active{color:var(--orange);font-weight:600}
.contact-btn{left:935px;top:35px;width:106px;height:36px;font-size:11px}
.badge{left:559px;top:190px;width:60px;height:60px;border-radius:50%;background:#1aa7d9;border:3px solid #fff}
.hero-title{left:0;width:1200px;top:262px;font-size:42px;font-weight:700;line-height:48px;color:#fff}
.hero-title em{font-style:normal;color:var(--orange)}
.hero-sub{left:0;width:1200px;top:364px;font-size:14px;color:#fff}
.hero-btn{left:523px;top:402px;width:154px;height:32px;font-size:11px}

.section-title{left:0;width:1200px;font-size:26px;font-weight:600;letter-spacing:.5px}
.lede{left:0;width:1200px;font-size:11.5px;line-height:15px;color:var(--muted)}

/* feature tiles */
.tile{top:780px;width:282px;height:164px;padding:62px 16px 0 16px;color:#fff}
.tile h3{font-size:17px;font-weight:600;margin-bottom:6px}
.tile p{font-size:10.5px;line-height:13px;width:190px}
.tile.dark{background:linear-gradient(135deg,#4a4339,#2a2d31)}
.tile.warm{background:linear-gradient(135deg,#f5a424,#e98e12)}
.tile.rich{background:linear-gradient(135deg,#3d3a37,#5c3530)}

.video{left:161px;top:968px;width:880px;height:320px;background:linear-gradient(180deg,#3d4753 0%,#4b4f48 55%,#3a2c26 100%)}

.mist{left:0;top:1290px;width:1200px;height:800px;background:linear-gradient(180deg,#fff 0%,#eef0f3 25%,#f4f5f7 60%,#fff 100%)}

/* pricing */
.price{top:1428px;width:259px;height:427px;background:linear-gradient(180deg,#2f2f31 0%,#3a3732 55%,#4d3c34 100%);box-shadow:0 8px 18px rgba(0,0,0,.25);color:#d9dadc;text-align:center;padding-top:18px}
.price h3{color:var(--orange);font-size:17px;font-weight:600}
.price .rule{width:30px;height:3px;background:var(--orange);margin:10px auto 8px}
.price .cost{color:#fff;font-size:13.5px;font-weight:600;line-height:17px}
.price ul{list-style:none;font-size:12.5px;line-height:16px;margin-top:10px;font-weight:300}
.price li{margin-bottom:8px}
.price .btn{position:absolute;left:78px;bottom:26px;width:103px;height:31px}

/* spots */
.spots-band{left:0;top:2075px;width:1200px;height:500px;background:linear-gradient(180deg,#5f6d84 0%,#6c7688 35%,#5b5148 60%,#d8d4d0 88%,#fff 100%)}
.spot{width:206px;height:291px;background:#fff;box-shadow:0 4px 14px rgba(0,0,0,.12)}
.spot .photo{width:100%;height:188px;background:linear-gradient(180deg,#7c8791,#3f4a52)}
.spot .play{position:absolute;left:84px;top:74px}
.spot .btn{left:42px;top:175px;width:122px;height:26px;font-size:10.5px}
.spot h4{position:absolute;top:218px;width:100%;text-align:center;font-size:15px;font-weight:600;line-height:18px}

/* testimonials */
.quote{width:250px}
.avatar{width:69px;height:64px;background:linear-gradient(180deg,#c9b9a8,#8a7766)}
.quote .name{position:absolute;left:88px;top:4px;font-size:17px;line-height:23px;font-weight:500;text-transform:uppercase}
.quote .date{position:absolute;left:88px;top:52px;font-size:17px;font-weight:400}
.quote .mark{position:absolute;left:0;top:74px;color:var(--orange);font-size:18px;font-weight:700}
.quote p{position:absolute;left:2px;top:100px;width:245px;font-size:11.5px;line-height:25.5px;color:#555}

/* gift */
.gift-photo{left:161px;top:3024px;width:447px;height:316px;background:linear-gradient(180deg,#6f8c74 0%,#5d7c86 35%,#b9453f 70%,#c9a36a 100%);box-shadow:0 6px 16px rgba(0,0,0,.2)}
.gift-title{left:685px;top:3054px;font-size:26px;font-weight:500}
.gift-copy{left:686px;top:3106px;width:345px;font-size:11.5px;line-height:14.5px;color:var(--muted)}
.gift-copy p{margin-bottom:15px}

/* lower */
.ridge{left:0;top:3470px;width:1200px;height:155px;background:linear-gradient(180deg,rgba(255,255,255,0) 0%,#7d8592 45%,#4b4f58 100%)}
.footer{left:0;top:3620px;width:1200px;height:463px;background:var(--footer)}
.footer-base{left:0;top:4083px;width:1200px;height:60px;background:var(--footer-deep)}
.f-brand{left:162px;top:3774px;font-size:20px;font-weight:700;color:var(--orange)}
.f-row{left:162px;display:flex;align-items:center;color:#fff;font-size:13.5px}
.f-row svg{margin-right:15px;flex:none}
.social{left:162px;top:3989px;display:flex;gap:18px}
.social span{width:12px;height:12px;border-radius:50%;background:#fff;display:block}
.f-nav{left:162px;top:4038px;font-size:12.5px;color:#fff}
.f-nav span{position:absolute;white-space:nowrap}
.copy{top:4092px;font-size:10px;color:#fff}

.form{left:621px;top:3568px;width:434px;height:502px;background:#fff;border-top:9px solid var(--orange);box-shadow:0 6px 18px rgba(0,0,0,.15)}
.form h3{position:absolute;top:34px;width:100%;text-align:center;color:var(--orange);font-size:27px;font-weight:400}
.field{position:absolute;left:43px;width:348px;border:1px solid var(--field);font-size:10px;color:#888;padding:12px 20px}
.send{left:43px;top:404px;width:348px;height:49px;border-radius:0;font-size:16px;font-weight:400}
</style>
</head>
<body>

<!-- HERO -->
<div class="abs hero" role="img" aria-label="Couple sharing red wine at a luxury clifftop picnic with flowers and a wicker basket"></div>
<div class="abs brand"><div>PICNIC WAYFARE</div></div>
<nav class="abs nav">
  <span class="active" style="left:0">Home</span>
  <span style="left:66px">As Seen on</span>
  <span style="left:169px">picnic spots</span>
  <span style="left:280px">testimonial</span>
  <span style="left:386px">gift certificates</span>
  <span style="left:511px">covid-19</span>
</nav>
<div class="btn contact-btn">CONTACT US</div>
<div class="abs badge" aria-label="Safety certification badge"></div>
<h1 class="abs hero-title center">SHARE AN <em>UNFORGETTABLE</em><br>MOMENT</h1>
<p class="abs hero-sub center">Luxury picnics at breathtaking locations</p>
<div class="btn hero-btn">BOOK YOUR PICNIC</div>

<!-- AS SEEN ON -->
<h2 class="abs section-title center" style="top:655px">AS SEEN ON</h2>
<p class="abs lede center" style="top:701px">Small strip saying ‘As Seen On’ with logos underneath -<br>we only have 1 for now being Crimson Kite</p>

<div class="abs tile dark" style="left:161px" role="img" aria-label="Friends enjoying a picnic outdoors"><h3>BLISS</h3><p>We enable you to enjoy true quality time with your partner, friends or family.</p></div>
<div class="abs tile warm" style="left:460px" role="img" aria-label="Couple embracing at sunset"><h3>UNWIND</h3><p>Let us do everything for you so you can enjoy a stress free experience.</p></div>
<div class="abs tile rich" style="left:759px" role="img" aria-label="Spread of gourmet picnic food"><h3>INDULGE</h3><p>Our delicious picnics will have your mouth watering! You can design your own picnic</p></div>

<div class="abs video" role="img" aria-label="Video still of a couple overlooking a mountain valley beside a picnic setup"></div>
<svg class="abs" style="left:571px;top:1100px" width="58" height="58" viewBox="0 0 58 58"><circle cx="29" cy="29" r="26" fill="none" stroke="#fff" stroke-width="3"/><path d="M23 18 L40 29 L23 40 Z" fill="#fff"/></svg>

<!-- PRICING -->
<div class="abs mist" role="img" aria-label="Faint misty mountain backdrop"></div>
<h2 class="abs section-title" style="top:1340px;left:0;width:1164px;text-align:center">OUR PRICING</h2>

<div class="abs price" style="left:167px">
  <h3>BYO PICNIC</h3><div class="rule"></div>
  <div class="cost">$200 + GST<br>HIR</div>
  <ul><li>transport and setup<br>of picnic equipment</li><li>directions to ‘secret’<br>location</li><li>2 hour picni</li><li>cleaning and pack up</li><li>still or sparkling water<br>cooled on ice with<br>glassware</li><li>BYO additional food<br>&amp; beverages</li></ul>
  <div class="btn">Read More</div>
</div>
<div class="abs price" style="left:473px">
  <h3>GOURMET PICNIC</h3><div class="rule"></div>
  <div class="cost">$200 + GST<br>HIR</div>
  <ul><li>transport and setup<br>of picnic equipment</li><li>directions to ‘secret’<br>location</li><li>2 hour picni</li><li>cleaning and pack up</li><li>still or sparkling water<br>cooled on ice with<br>glassware</li><li>BYO additional food<br>&amp; beverages</li></ul>
  <div class="btn">Read More</div>
</div>
<div class="abs price" style="left:779px">
  <h3>PROPOSAL PICNIC</h3><div class="rule"></div>
  <div class="cost">$200 + GST<br>HIR</div>
  <ul><li>transport and setup<br>of picnic equipment</li><li>directions to ‘secret’<br>location</li><li>2 hour picni</li><li>cleaning and pack up</li><li>still or sparkling water<br>cooled on ice with<br>glassware</li><li>BYO additional food<br>&amp; beverages</li></ul>
  <div class="btn">Read More</div>
</div>

<!-- PICNIC SPOTS -->
<h2 class="abs section-title" style="top:1907px;left:0;width:1254px;text-align:center">PICNIC SPOTS</h2>
<p class="abs lede" style="top:1961px;left:0;width:1234px;text-align:center">You will love our breathtaking locations which you won’t find on Mapfinder! The only way to<br>experience these stunning spots first hand is by organising a picnic with us.</p>
<p class="abs lede" style="top:2007px;left:0;width:1234px;text-align:center">We have handpicked the absolute best picnic spots in the Blue Mountains from years<br>of local knowledge. They’re all accessible with regular vehicles and only a short walk<br>from where you park. Our spots are very quiet giving you a peaceful<br>and unique glimpse of the Blue Mountains.</p>

<div class="abs spots-band" role="img" aria-label="Couple seen from behind looking across a blue mountain range"></div>

<div class="abs spot" style="left:161px;top:2312px">
  <div class="photo" role="img" aria-label="Misty lookout over a river bend"></div>
  <svg class="abs play" width="38" height="38" viewBox="0 0 38 38"><circle cx="19" cy="19" r="16" fill="none" stroke="#fff" stroke-width="2.5"/><path d="M15 11 L27 19 L15 27 Z" fill="#fff"/></svg>
  <div class="btn">View Available</div><h4>Katoomba Picnic<br>Spot</h4>
</div>
<div class="abs spot" style="left:383px;top:2287px">
  <div class="photo" role="img" aria-label="Lakeside cabin under misty hills"></div>
  <svg class="abs play" width="38" height="38" viewBox="0 0 38 38"><circle cx="19" cy="19" r="16" fill="none" stroke="#fff" stroke-width="2.5"/><path d="M15 11 L27 19 L15 27 Z" fill="#fff"/></svg>
  <div class="btn">View Available</div><h4>Katoomba Picnic<br>Spot</h4>
</div>
<div class="abs spot" style="left:603px;top:2312px">
  <div class="photo" style="background:linear-gradient(180deg,#5f7a7e,#2f4b3e)" role="img" aria-label="Green cliffs rising above calm water"></div>
  <svg class="abs play" width="38" height="38" viewBox="0 0 38 38"><circle cx="19" cy="19" r="16" fill="none" stroke="#fff" stroke-width="2.5"/><path d="M15 11 L27 19 L15 27 Z" fill="#fff"/></svg>
  <div class="btn">View Available</div><h4>Katoomba Picnic<br>Spot</h4>
</div>
<div class="abs spot" style="left:824px;top:2287px">
  <div class="photo" style="background:linear-gradient(180deg,#8fa3ad,#5a6a58 55%,#8a5a4a)" role="img" aria-label="Poolside loungers at a resort"></div>
  <svg class="abs play" width="38" height="38" viewBox="0 0 38 38"><circle cx="19" cy="19" r="16" fill="none" stroke="#fff" stroke-width="2.5"/><path d="M15 11 L27 19 L15 27 Z" fill="#fff"/></svg>
  <div class="btn">View Available</div><h4>Katoomba Picnic<br>Spot</h4>
</div>

<!-- TESTIMONIAL -->
<h2 class="abs section-title center" style="top:2673px">TESTIMONIAL</h2>

<div class="abs quote" style="left:161px;top:2767px">
  <div class="avatar" role="img" aria-label="Customer portrait"></div>
  <div class="name">Marisol<br>Vantega</div><div class="date">05 JAN 2020</div>
  <div class="mark">“</div>
  <p>Lorem ipsum dolor sit amet, consecte-<br>tur adipiscing elit, sed do eiusmod<br>tempor incididunt ut</p>
</div>
<div class="abs quote" style="left:473px;top:2767px">
  <div class="avatar" role="img" aria-label="Customer portrait"></div>
  <div class="name">Oriana<br>Petrakis</div><div class="date">05 JAN 2020</div>
  <div class="mark">“</div>
  <p>Lorem ipsum dolor sit amet, consecte-<br>tur adipiscing elit, sed do eiusmod<br>tempor incididunt ut</p>
</div>
<div class="abs quote" style="left:777px;top:2767px">
  <div class="avatar" role="img" aria-label="Customer portrait"></div>
  <div class="name">Marisol<br>Vantega</div><div class="date">05 JAN 2020</div>
  <div class="mark">“</div>
  <p>Lorem ipsum dolor sit amet, consecte-<br>tur adipiscing elit, sed do eiusmod<br>tempor incididunt ut</p>
</div>

<!-- GIFT CERTIFICATES -->
<div class="abs gift-photo" role="img" aria-label="Picnic basket with wine, grapes and food on a checked cloth beside a lake"></div>
<h2 class="abs gift-title">GIFT CERTIFICATES</h2>
<div class="abs gift-copy">
  <p>Do you struggle for gift ideas? Worried about wasting your money on something they won’t like?</p>
  <p>Our picnics are a unique and memorable gift that everyone will love!</p>
  <p>We can mail you a professionally printed Gift Certificate at no extra cost!</p>
  <p>We also offer Payment Plans on Gift Certificates</p>
</div>
<div class="btn" style="left:685px;top:3277px;width:155px;height:32px;font-size:11px">BOOK YOUR PICNIC</div>

<!-- FAQ -->
<div class="abs ridge" role="img" aria-label="Blue Mountains escarpment at dusk"></div>
<h2 class="abs section-title center" style="top:3402px;font-weight:600">FREQUENTLY ASKED QUESTIONS</h2>
<p class="abs lede center" style="top:3445px;color:#444">Lorem ipsum dolor sit amet, consectetur adipiscing elit,<br>sed do eiusmod tempor incididunt ut labore et dolore</p>
<div class="btn" style="left:550px;top:3489px;width:102px;height:31px;font-size:11px;font-weight:500">GO TO FAQ</div>

<!-- FOOTER -->
<div class="abs footer"></div>
<div class="abs footer-base"></div>
<div class="abs f-brand">PICNIC WAYFARE</div>
<div class="abs f-row" style="top:3821px"><svg width="26" height="26" viewBox="0 0 26 26"><circle cx="13" cy="13" r="13" fill="var(--orange)"/><path d="M9 7c1 0 2 2.5 2 3s-1 1-1 1.6 2 3.4 3.4 3.4c.6 0 1-1 1.6-1s3 1 3 2-1.5 2-2.5 2C11 18 8 14 8 9.5 8 8 8.5 7 9 7z" fill="#fff"/></svg>555-014-2200</div>
<div class="abs f-row" style="top:3865px"><svg width="26" height="26" viewBox="0 0 26 26"><circle cx="13" cy="13" r="13" fill="var(--orange)"/><path d="M9 7c1 0 2 2.5 2 3s-1 1-1 1.6 2 3.4 3.4 3.4c.6 0 1-1 1.6-1s3 1 3 2-1.5 2-2.5 2C11 18 8 14 8 9.5 8 8 8.5 7 9 7z" fill="#fff"/></svg>555-014-7731</div>
<div class="abs f-row" style="top:3909px;font-size:11px;line-height:13px;align-items:flex-start"><svg width="26" height="26" viewBox="0 0 26 26"><circle cx="13" cy="13" r="12" fill="none" stroke="var(--orange)" stroke-width="1.5"/><path d="M13 6a4.5 4.5 0 0 0-4.5 4.5C8.5 14 13 19.5 13 19.5s4.5-5.5 4.5-9A4.5 4.5 0 0 0 13 6zm0 6.2a1.7 1.7 0 1 1 0-3.4 1.7 1.7 0 0 1 0 3.4z" fill="var(--orange)"/></svg><span>Picnic Wayfare office<br>18 Fernhollow Lane<br>Ridgecombe, NSW 2999</span></div>
<div class="abs social" aria-label="Social links"><span></span><span></span><span></span><span></span><span></span></div>
<nav class="abs f-nav">
  <span style="left:0;color:var(--orange);font-weight:600">Home</span>
  <span style="left:55px">As Seen on</span>
  <span style="left:141px">picnic spots</span>
  <span style="left:248px">testimonial</span>
  <span style="left:350px">Blog</span>
</nav>
<div class="abs copy" style="left:162px">© 2020 picnic wayfare. All rights reserved.</div>
<div class="abs copy" style="left:821px">Accessibility Notice | Privacy Policy | Site map</div>

<!-- CONTACT FORM -->
<form class="abs form">
  <h3>Send Us a Message</h3>
  <div class="field" style="top:83px;height:47px">Name</div>
  <div class="field" style="top:142px;height:48px">Phone</div>
  <div class="field" style="top:203px;height:48px">Email</div>
  <div class="field" style="top:263px;height:133px">Message</div>
  <div class="btn send">Send Message</div>
</form>

</body>
</html>
```